Home Page Redesign for Pet Website

Looking to redesign the home page of our WORDPRESS website which will be renamed The Critter Cover Handbook 2015.

Looking for clean design which communicates clarity.
Updates

This is for a Wordpress site.

Please note that the design MUST include the content which is shown in the table in the brief!

Hi Thanks for the designs so far. We have just updated the brief to provide more information and clarify a few issues. We have also now included a couple of layout suggestions. They are just suggestions but it should give you a better idea of what we are looking for. And we have just increased the budget for 1st place by £120. Please feel free to message me if you have any questions. Many thanks. Maud

Please note that the new brief is in a file dated 25 Jan!

Reason: We have extended the deadline so we can continue working with the designers who have submitted designs we like. If you have any new designs please submit them by the original deadline of 7.37pm this evening (GMT). We are planning to make our final decision by Friday this week.

Target Market(s)

UK pet owners. All ages but largest age group is 35-50.

Industry/Entity Type

Insurance

Requirements
Must have
• Three clear content groups - LEARN, RESEARCH, CAMPAIGN (see brief for more details).
Stock photos with dogs and cats
Use current colour scheme
Must work with existing inner pages.
Existing font.. but 1pt larger
See brief for more details
Should not have
• Logo
Content from Existing Page (except for footer content... and menu headings).

```html
<!DOCTYPE html>
<html lang="en">
<head>
<meta charset="utf-8">
<title>The Critter Cover Handbook 2015</title>
<link rel="stylesheet" href="https://fonts.googleapis.com/css2?family=Roboto+Slab:wght@400;700&family=Open+Sans:ital,wght@0,400;0,600;0,700;1,600&display=swap">
<style>
:root{
  --blue:#0d5aa7;
  --navy:#0b3c6e;
  --deep:#1c3d86;
  --orange:#f7892b;
  --purple:#a25be0;
  --green:#5aa86c;
  --ink:#3a3a3a;
  --muted:#6a6a6a;
  --panel:#f1f1f1;
  --line:#d8d8d8;
  --red:#b4161d;
}
*{box-sizing:border-box;margin:0;padding:0}
html,body{width:695px;height:1200px;overflow:hidden}
body{position:relative;background:#fff;font-family:"Open Sans",Arial,sans-serif;color:var(--ink);font-size:7.4px;line-height:1.45}
.abs{position:absolute}
.topline{left:0;top:0;width:695px;height:2px;background:var(--blue)}
.brand{left:92px;top:14px;display:flex;align-items:center;gap:6px}
.brand .dot{width:33px;height:33px;border-radius:50%;background:var(--blue)}
.brand .name{font-family:"Roboto Slab",serif;font-weight:700;font-size:13px;line-height:1.15;color:var(--deep);width:170px;text-transform:uppercase}
.phone{left:513px;top:8px;font-size:12px;color:#222;display:flex;align-items:center;gap:4px}
.search{left:462px;top:32px;width:118px;height:15px;border:1px solid #ccc;font-size:6px;color:#aaa;padding:3px 4px}
.go{left:584px;top:32px;width:24px;height:15px;background:var(--blue);color:#fff;font-weight:700;font-size:8px;text-align:center;line-height:15px}
.nav{left:0;top:54px;width:695px;height:28px;background:var(--blue);display:flex;padding-left:86px}
.nav a{display:block;height:28px;line-height:28px;padding:0 9px;color:#fff;font-size:8px;text-decoration:none}
.nav .home{color:#111}
.nav .learn{background:var(--orange)}
.nav .research{background:var(--purple)}
.nav .campaign{background:var(--navy)}
.hero{left:0;top:82px;width:695px;height:189px;background:linear-gradient(180deg,#2f5ab0,#1c3d86)}
.hero-photo{left:118px;top:0;width:340px;height:189px;background:radial-gradient(ellipse at 50% 60%,#c78f52 0%,#9b6c45 40%,rgba(60,60,90,0) 72%)}
.hero h1{right:101px;top:56px;font-family:"Roboto Slab",serif;font-weight:700;font-size:15px;line-height:23px;color:#fff;text-align:right}
.arrow{width:19px;height:19px;top:159px}
.arrow.l{left:66px;background:#8b95a8}
.arrow.r{left:608px;background:#4f8fe0}
.box{position:absolute;left:78px;width:339px;background:linear-gradient(90deg,#f6f6f6,#e7e7e7 60%,#f4f4f4)}
.box h2{height:21px;line-height:21px;padding-left:6px;font-family:"Roboto Slab",serif;font-weight:400;font-size:10px;color:#fff}
.box h2 b{font-weight:700}
.box .in{padding:6px 7px 0}
.h-orange{background:var(--orange)}
.h-purple{background:var(--purple)}
.h-navy{background:var(--navy)}
.h-green{background:var(--green)}
.h-blue{background:var(--blue)}
.cols{display:flex;margin-top:6px}
.cols ul{list-style:none;width:50%}
.cols li{position:relative;padding-left:13px;margin-bottom:4.5px;font-size:7.5px;color:#444}
.cols li::before{content:"";position:absolute;left:2px;top:2px;width:6px;height:6px;border:1px solid var(--orange);border-radius:50%;box-shadow:inset 0 0 0 1.5px #f6f6f6,inset 0 0 0 3px var(--orange)}
.more{position:absolute;right:13px;font-family:"Roboto Slab",serif;font-size:7.5px;color:#444;border-bottom:1px solid #888}
.cta{font-family:"Open Sans",sans-serif;font-style:italic;font-weight:600;font-size:9.2px;color:#333;line-height:15px;margin-top:8px}
.side{position:absolute;left:430px;width:178px;background:#f4f4f4;border:1px solid var(--line)}
.side h3{height:21px;line-height:21px;padding-left:7px;font-family:"Roboto Slab",serif;font-weight:400;font-size:10px;color:#fff;margin:-1px -1px 0}
.side .in{padding:6px 7px}
.ad{position:absolute;left:431px;width:177px;background:#fff;border:1px solid #ccc;overflow:hidden}
.ad .mark{font-family:"Roboto Slab",serif;font-size:23px;color:#8c8c8c;text-align:center;line-height:28px}
.ad .tag{font-family:"Roboto Slab",serif;font-size:8.5px;color:#555;text-align:center}
.ad .pup{position:absolute;left:2px;background:radial-gradient(ellipse,#b0672e,#d99a5c 45%,rgba(255,255,255,0) 72%)}
.ad .ticks{position:absolute;left:82px;list-style:none;color:var(--red);font-size:8px;line-height:9px}
.ad .ticks li{position:relative;padding-left:18px;margin-bottom:4px}
.ad .ticks svg{position:absolute;left:0;top:0}
.ad .quote{position:absolute;left:89px;background:var(--red);color:#fff;font-weight:700;font-size:7.5px;text-align:center;border-radius:2px}
.ad .off{position:absolute;left:78px;font-weight:700;font-size:7.8px;color:#111}
.ad .fine{position:absolute;left:0;width:100%;text-align:center;font-size:5.6px;color:#888;background:#f0f0f0}
.footer{left:0;top:954px;width:695px;height:222px;background:linear-gradient(180deg,#2c4fa0,#1c3a82)}
.widget{position:absolute;top:970px;width:152px;height:190px;background:#fff;border-radius:3px;overflow:hidden}
.widget .wh{height:20px;line-height:20px;padding-left:8px;font-family:"Roboto Slab",serif;font-weight:700;font-size:9.5px;color:var(--deep)}
.fb .wh{background:#dfe4ee}
.tw .wh{background:#5fc2df}
.widget .tiny{font-size:6px;line-height:8px;color:#333}
.avatar{width:22px;height:22px;background:#c9b8a8;display:inline-block}
.follow-h{left:443px;top:971px;font-family:"Roboto Slab",serif;font-size:10px;color:#fff}
.fbtn{position:absolute;left:443px;background:#fff;border:1px solid #bbb;border-radius:2px;font-weight:700;color:#223;height:17px;line-height:16px;padding:0 6px;font-size:9.5px;display:flex;align-items:center;gap:4px}
.fbtn i{width:10px;height:10px;display:inline-block}
.footer-title{left:443px;top:1111px;width:160px;text-align:center;font-family:"Roboto Slab",serif;font-weight:700;font-size:13px;line-height:18px;color:#111;text-transform:uppercase}
.bottom{left:0;top:1176px;width:695px;height:24px;background:#0c0c0c;color:#ddd;font-size:6.3px;text-align:center;line-height:24px}
.pet{position:absolute}
</style>
</head>
<body>
<div class="abs topline"></div>

<header>
  <div class="abs brand"><span class="dot"></span><span class="name">The Critter Cover Handbook 2015</span></div>
  <div class="abs phone">
    <svg width="11" height="11" viewBox="0 0 12 12"><circle cx="6" cy="6" r="5.3" fill="none" stroke="#222" stroke-width="1"/><path d="M4 3.2l1 1.3-.6.8c.4.9 1 1.5 1.9 1.9l.8-.6 1.3 1-.6 1C6 8.5 3.5 6 3 4.1z" fill="#222"/></svg>
    <span>555-014-2015</span>
  </div>
  <div class="abs search">search here......</div>
  <div class="abs go">GO</div>
  <nav class="abs nav">
    <a class="home" href="#">HOME</a>
    <a class="learn" href="#">LEARN About Pet Insurance</a>
    <a class="research" href="#">RESEARCH Pet Insurance Policies</a>
    <a class="campaign" href="#">CAMPAIGN For Fairer Pet Insurance</a>
    <a href="#">CONTACT US</a>
  </nav>
</header>

<section class="abs hero">
  <div class="abs hero-photo" role="img" aria-label="Photo of two puppies and two kittens sitting in a row"></div>
  <h1 class="abs">Independent Unbiased<br>Information For<br>Fellow Pet Owners</h1>
</section>
<svg class="abs arrow l" viewBox="0 0 19 19"><rect width="19" height="19" fill="#8b95a8"/><path d="M11 5l-4 4.5 4 4.5" stroke="#fff" stroke-width="1.5" fill="none"/></svg>
<svg class="abs arrow r" viewBox="0 0 19 19"><rect width="19" height="19" fill="#4f8fe0"/><path d="M8 5l4 4.5-4 4.5" stroke="#fff" stroke-width="1.5" fill="none"/></svg>

<main>
  <section class="box" style="top:293px;height:153px">
    <h2 class="h-orange">LEARN <b>About Pet Insurance</b></h2>
    <div class="in">
      <p>Lorem ipsum dolor sit amet, consectetuer adipiscing elit, sed diam nonummy nibh isaincidunt ut laoreet dolore magna aliquam erat volutpat. Ut wisi enim ad minim veniam, quisstruexerci tation ullamcorper suscipit lobortis nisl ut aliquip accumsan et iusto odio enim..</p>
      <div class="cols">
        <ul>
          <li>Vet Fees Cover Types</li>
          <li>What to Consider before Buying</li>
          <li>Ten Popular Pet Insurance Providers</li>
          <li>Confused by Pet Insurance:&nbsp; Start Here!</li>
          <li>Third Party Liability Insurance</li>
        </ul>
        <ul>
          <li>Six Vet Fees Pet Insurance Companies Won't Pay!</li>
          <li>Why Cheap Pet Insurance is Risky</li>
          <li>Why Your Pets Vet History is Important</li>
        </ul>
      </div>
    </div>
    <span class="more" style="bottom:8px">Read More</span>
  </section>

  <section class="box" style="top:463px;height:214px">
    <h2 class="h-purple">Research <b>UK Pet Insurance Policies</b></h2>
    <div class="in">
      <p style="font-size:7.6px;color:#222">Analysis, Customer Reviews and Full Details of All UK Policies</p>
      <div class="cols">
        <ul>
          <li>Burrow Friends</li><li>Arcade</li><li>Straight Wire</li><li>F&amp;M</li>
          <li>Hale Paws</li><li>Helpwell Cover</li><li>James Lowry</li><li>MV= Mersey Victory</li>
        </ul>
        <ul>
          <li>Kennel Guild</li><li>N&amp;T</li><li>Over And Above Pet Insurance</li><li>Tailplan</li>
          <li>Saltbury's Finance</li><li>Tolvo</li><li>Vireo Money</li><li>Other Providers</li>
        </ul>
      </div>
      <p class="cta">Search Our Database For Policies Matching Your Criteria<br>Compare Claims Experiences&nbsp; For Pet Insurance Providers</p>
    </div>
    <span class="more" style="bottom:12px">Read More</span>
  </section>

  <section class="box" style="top:692px;height:150px">
    <h2 class="h-navy">Campaign <b>For Fairer Pet Insurance</b></h2>
    <div class="in" style="padding:10px 8px 0">
      <p>Loremre ipsum dolor sit amet, consectetuer adipiscing elit, sed diam nonummy nibh rerunt ut laoreet dolore magna aliquam erat volutpat. Ut wisi enim ad minim veniam, quis loremis nostruexerci tation ullamcorper suscipit lobortis nisl.</p>
      <p style="margin-top:3px">Loremre ipsum dolor sit amet, consectetuer adipiscing elit, sed diam nonummy nibh rerunt ut laoreet dolore magna aliquam erat volutpat.</p>
      <p style="margin-top:8px">Loremre ipsum dolor sit amet, consectetuer adipiscing elit, sed diam nonummy nibh rerunt ut laoreet dolore magna aliquam erat volutpat. Ut wisi enim ad minim veniam, quis loremis nostruexerci tation ullamcorper suscipit.</p>
    </div>
    <span class="more" style="bottom:7px">Read More</span>
  </section>

  <section class="box" style="top:859px;height:71px">
    <h2 class="h-green">Popular <b>Resources</b></h2>
    <div class="in">
      <p>Loremre ipsum dolor sit amet, consectetuer adipiscing elit, sed diam nonummy nibh rerunt ut laoreet dolore magna aliquam erat volutpat.</p>
      <div class="cols" style="margin-top:4px"><ul style="width:85px"><li style="font-size:8px">Lorem Ipsum</li></ul><ul><li style="font-size:8px">Lorem Ipsum</li></ul></div>
    </div>
    <span class="more" style="bottom:8px">Read More</span>
  </section>
</main>

<aside>
  <div class="ad" style="top:293px;height:155px">
    <div class="mark">pawshield</div>
    <div class="tag">Medical insurance for your pet.</div>
    <div class="pup" role="img" aria-label="Photo of a puppy with a ball" style="top:40px;width:80px;height:95px"></div>
    <ul class="ticks" style="top:48px">
      <li><svg width="14" height="12" viewBox="0 0 14 12"><path d="M1 6l4 4 8-9" stroke="#b4161d" stroke-width="2.4" fill="none"/></svg>One<br>Simple Plan</li>
      <li><svg width="14" height="12" viewBox="0 0 14 12"><path d="M1 6l4 4 8-9" stroke="#b4161d" stroke-width="2.4" fill="none"/></svg>90% Coverage</li>
      <li><svg width="14" height="12" viewBox="0 0 14 12"><path d="M1 6l4 4 8-9" stroke="#b4161d" stroke-width="2.4" fill="none"/></svg>No<br>Payout Limits</li>
    </ul>
    <div class="quote" style="top:112px;width:66px;height:17px;line-height:17px">FREE QUOTE ▸</div>
    <div class="off" style="top:133px">Get $10 off enrollment</div>
    <div class="fine" style="top:146px;height:9px;line-height:9px">Exclusions may apply. See policy for full details.</div>
  </div>

  <section class="side" style="top:465px;height:173px">
    <h3 class="h-blue">Biography</h3>
    <div class="in">
      <div style="display:flex;gap:22px">
        <div role="img" aria-label="Portrait photo of a puppy in a circle" style="width:55px;height:54px;border-radius:50%;background:radial-gradient(circle,#7a5a3c,#c8d6e8 70%)"></div>
        <div style="font-size:7.2px;padding-top:6px">Lorem Ipsum<br>Autem<br><br>Lorem Isum, Autem</div>
      </div>
      <p style="font-size:6.3px;margin-top:5px">Ut wisi enim ad minim veniam, quis nostrud exerc ree orper suscipit lobortis nisl ut aliquip ex ea commodor consequat. Duis autem vel eum. Lorem ipsum is ther dummpy text of the insustry.</p>
      <p style="font-size:6.3px;margin-top:3px">Ut wisi enim ad minim veniam, quis nostrud exerc ullamcade orper suscipit lobortis.</p>
    </div>
    <span class="more" style="bottom:8px;right:15px">Read More</span>
  </section>

  <section class="side" style="top:656px;height:141px;background:#fff">
    <h3 class="h-green">Disclaimer</h3>
    <div class="in" style="font-size:6.6px;line-height:10.5px">
      <p>Please note that pet insurance terms often change. Whilst we will do our best to keep this website up to date you must check with the appropriate insurer before making any decisions. If you find any mistakes on this website please do let us know so we can correct it for the benefit of future visitors. Many thanks! -</p>
      <p style="margin-top:2px">See more at:<br>www.critter-cover-polls.example/insurers/#ref.k7QmB2</p>
    </div>
  </section>

  <div class="ad" style="top:813px;height:117px">
    <div class="mark" style="font-size:21px;line-height:25px">pawshield</div>
    <div class="tag" style="font-size:7.5px">Medical insurance for your pet.</div>
    <div class="pup" role="img" aria-label="Photo of a puppy with a ball" style="top:34px;width:80px;height:72px"></div>
    <ul class="ticks" style="top:38px;font-size:7px;line-height:8px">
      <li style="margin-bottom:1px"><svg width="14" height="12" viewBox="0 0 14 12"><path d="M1 6l4 4 8-9" stroke="#b4161d" stroke-width="2.4" fill="none"/></svg>One<br>Simple Plan</li>
      <li style="margin-bottom:2px"><svg width="14" height="12" viewBox="0 0 14 12"><path d="M1 6l4 4 8-9" stroke="#b4161d" stroke-width="2.4" fill="none"/></svg>90% Coverage</li>
      <li><svg width="14" height="12" viewBox="0 0 14 12"><path d="M1 6l4 4 8-9" stroke="#b4161d" stroke-width="2.4" fill="none"/></svg>No<br>Payout Limits</li>
    </ul>
    <div class="quote" style="top:85px;width:66px;height:13px;line-height:13px;font-size:6.8px">FREE QUOTE ▸</div>
    <div class="off" style="top:99px;font-size:7px">Get $10 off enrollment</div>
    <div class="fine" style="top:109px;height:8px;line-height:8px">Exclusions may apply. See policy for full details.</div>
  </div>
</aside>

<div class="pet" role="img" aria-label="Photo of a sitting German shepherd dog" style="left:12px;top:868px;width:58px;height:86px;background:radial-gradient(ellipse at 50% 55%,#7a5230,#b9864f 45%,rgba(255,255,255,0) 72%)"></div>
<div class="pet" role="img" aria-label="Photo of a cat looking upward" style="left:604px;top:832px;width:86px;height:122px;background:radial-gradient(ellipse at 50% 55%,#8a6a4e,#cfb08c 45%,rgba(255,255,255,0) 72%)"></div>

<footer>
  <div class="abs footer"></div>
  <svg class="abs" style="left:32px;top:956px" width="22" height="10" viewBox="0 0 22 10"><path d="M4 3h14M4 7h14" stroke="#fff" stroke-width="4" stroke-linecap="round"/></svg>

  <div class="widget fb" style="left:91px">
    <div class="wh">Join us on Pagebook</div>
    <div style="display:flex;gap:6px;padding:6px">
      <span class="avatar"></span>
      <div class="tiny"><b style="color:var(--deep);font-size:6.8px">Critter Cover Polls UK</b><br><span style="background:#4a66a0;color:#fff;padding:0 3px">Like</span> 1,176</div>
    </div>
    <div style="margin:2px 8px;border:1px solid #ddd;height:118px;padding:6px" class="tiny">
      <div style="display:flex;gap:5px"><span class="avatar"></span><div><b style="color:var(--deep);font-size:6.8px">Critter Cover Polls UK</b><br><span style="color:#999">January 18 at 11:43pm</span></div></div>
      <p style="margin-top:6px">Pet Insurance Premium Increases</p>
      <p style="margin-top:3px">Interesting article from Consumer Watch suggesting that pet insurance premiums can double as your pet ages...</p>
      <p style="margin-top:3px">Have to confess that this sounds on the low side to me! Would be really keen to hear how much yours rose.</p>
    </div>
  </div>

  <div class="widget tw" style="left:266px">
    <div class="wh" style="color:#1a3a80">Latest from Chirper</div>
    <div class="tiny" style="padding:4px 5px;display:flex;justify-content:space-between;border-bottom:1px solid #eee"><b style="font-size:6.8px">Tweets</b><span style="border:1px solid #ccc;padding:0 4px">Follow</span></div>
    <div class="tiny" style="padding:2px 6px"><span style="color:var(--blue)">srv.ly/4kQw</span></div>
    <div class="tiny" style="padding:5px 6px;border-top:1px solid #eee">
      <div style="display:flex;gap:4px"><span class="avatar" style="width:13px;height:13px"></span><div><b>Critter Cover Polls</b> <span style="color:#999">26 Sep</span><br><span style="color:#999">@CritterPolls</span></div></div>
      <p>Know someone who has made a pet insurance claim in the last year? Please ask them to tell us about it. Please RT!<br><span style="color:var(--blue)">lnk.ly/Q8R2</span><br><span style="color:#999">Expand</span></p>
    </div>
    <div class="tiny" style="padding:3px 6px;border-top:1px solid #eee"><b>Critter Cover Polls</b> <span style="color:#999">26 Sep</span></div>
    <div class="tiny" style="margin:4px 4px;border:1px solid #ccc;padding:3px;color:#999">Tweet to @CritterPolls</div>
  </div>

  <div class="abs follow-h">Follow Us</div>
  <div class="fbtn" style="top:994px"><i style="background:#4aa3df;border-radius:50%"></i>Follow @CritterPolls</div>
  <div class="fbtn" style="top:1016px;border:none"><i style="background:#4a66a0"></i>Like</div>
  <div class="fbtn" style="top:1038px;width:73px"><i style="background:#d34836"></i>Follow</div>
  <div class="abs footer-title">The Critter Cover Handbook 2015</div>

  <div class="abs bottom">Copyright © 2015.&nbsp; TheCritterCoverHandbook2015.&nbsp; All Rights Reserved.</div>
</footer>
</body>
</html>
```